Label design needed for a new brain focus supplement. Cervalique.com

Hi I’m looking for a quality label design for a my new supplement. The supplement is a nootropic (brain focus booster). I’ll also upload my competitors designs as a reference and to get some ideas.

I was thinking to use a white glossy background with the gold logo in top with some gold graphics added. Along with some focus driven text.

Dimensions for label are 300mm x 105mm Landscape. Please allow a 5mm safe text area.

Target Market(s)

High achieving focus driven People.

Font styles to use
Sans Serif

Colors

Designer to choose colors to be used in the design.

Requirements
Must have
• Good quality design.
Nice to have
• wording to use on label
• EXTREME FOCUS
• Brain food supplement
• High quality
• Premium blend
• Dietary supplement
Should not have
• Bright colourful colours. This is a premium product and label should show this

```html
<!DOCTYPE html>
<html lang="en">
<head>
<meta charset="utf-8">
<title>Nootropic – Extreme Focus Label</title>
<link rel="stylesheet" href="https://fonts.googleapis.com/css2?family=Saira+Semi+Condensed:wght@400;500&family=Saira:ital,wght@0,700;1,800&family=Tenor+Sans&display=swap">
<style>
  :root {
    --band-blue: #4c9af2;
    --pill-blue: #4a97f0;
    --ink: #111111;
    --paper: #ffffff;
    --tint-cyan: #c2f5f4;
    --tint-sky: #c0e2f8;
    --tint-periwinkle: #bdd0f8;
    --brain-cyan: #4fd6e6;
    --brain-blue: #3b8df0;
    --gold-light: #fff3b8;
    --gold-mid: #d9b650;
    --gold-deep: #9a7425;
    --gold-text: #8a6418;
  }
  * { margin: 0; padding: 0; box-sizing: border-box; }
  html, body { width: 1200px; height: 420px; overflow: hidden; background: var(--paper); }
  .label {
    position: relative;
    width: 1200px;
    height: 420px;
    background: var(--paper);
    overflow: hidden;
  }
  .band { position: absolute; left: 0; width: 100%; height: 15px; background: var(--band-blue); }
  .band--top { top: 0; }
  .band--bottom { bottom: 0; }

  .pattern-field {
    position: absolute;
    top: 15px;
    bottom: 15px;
    opacity: 0.9;
  }
  .pattern-field--left {
    left: 0; width: 529px;
    background: linear-gradient(30deg, var(--tint-cyan) 0%, var(--tint-sky) 50%, var(--tint-periwinkle) 100%);
  }
  .pattern-field--right {
    left: 671px; width: 529px;
    background: linear-gradient(30deg, var(--tint-cyan) 0%, var(--tint-sky) 55%, var(--tint-periwinkle) 100%);
  }

  .top-line {
    position: absolute;
    top: 36px;
    font-family: "Saira Semi Condensed", sans-serif;
    font-weight: 400;
    font-size: 24px;
    line-height: 1;
    color: var(--ink);
  }
  .top-line--type { left: 415px; }
  .top-line--count { left: 654px; font-weight: 500; }

  .brand-mark {
    position: absolute;
    left: 554px; top: 133px;
    width: 88px; height: 86px;
    border-radius: 40% 40% 30% 30%;
    background: linear-gradient(135deg, var(--brain-cyan), var(--brain-blue));
  }

  .product-name {
    position: absolute;
    left: 0; width: 1200px;
    top: 218px;
    text-align: center;
    font-family: "Tenor Sans", sans-serif;
    font-size: 45px;
    line-height: 1;
    color: var(--ink);
  }

  .claim-pill {
    position: absolute;
    left: 524px; top: 286px;
    width: 148px; height: 22px;
    border-radius: 11px;
    background: var(--pill-blue);
    color: var(--paper);
    font-family: "Saira", sans-serif;
    font-style: italic;
    font-weight: 800;
    font-size: 17px;
    line-height: 22px;
    text-align: center;
    letter-spacing: 0.3px;
  }

  .seal {
    position: absolute;
    top: 331px;
    width: 68px; height: 68px;
    border-radius: 50%;
    background: radial-gradient(circle at 40% 30%, var(--gold-light) 0%, var(--gold-mid) 60%, var(--gold-deep) 100%);
    box-shadow: inset 0 0 0 3px var(--gold-deep), inset 0 0 0 5px var(--gold-light);
    display: flex;
    align-items: center;
    justify-content: center;
    text-align: center;
    font-family: "Saira", sans-serif;
    font-weight: 700;
    color: var(--gold-text);
    line-height: 1.05;
  }
  .seal--brain-food { left: 481px; font-size: 8.5px; }
  .seal--premium { left: 564px; font-size: 11px; }
  .seal--quality { left: 648px; font-size: 12.5px; }
</style>
</head>
<body>
  <div class="label">
    <div class="band band--top"></div>

    <div class="pattern-field pattern-field--left" role="img" aria-label="Soft hexagon tile pattern in pale cyan and periwinkle"></div>
    <div class="pattern-field pattern-field--right" role="img" aria-label="Soft hexagon tile pattern in pale cyan and periwinkle"></div>

    <p class="top-line top-line--type">Dietary supplement</p>
    <p class="top-line top-line--count">60 CAPSULES</p>

    <div class="brand-mark" role="img" aria-label="Blue brain emblem with circuit lines"></div>

    <h1 class="product-name">Nootropic</h1>

    <p class="claim-pill">EXTREME FOCUS</p>

    <div class="seal seal--brain-food">BRAIN FOOD<br>SUPPLEMENT</div>
    <div class="seal seal--premium">PREMIUM<br>BLEND</div>
    <div class="seal seal--quality">HIGH<br>QUALITY</div>

    <div class="band band--bottom"></div>
  </div>
</body>
</html>
```